Van & Truck Wraps for Commercial Fence Company in Massachusetts

Looking for a design wrap for our 2020 Corvane Vans and also our Halden R260 - they are white vans and trucks - see attached designs and colors i got from my local shop and they dont stand out enough or really do much for me.
We specialize in commercial fence / temp fence and gate automation and access controls with a heavy influence on gate automation and access controls from Hinge Vista (HVS) you can see our colors and logo on www.harborlinefenceandpostco.com
I want something that is classy but still pops as an advertising bulletin as we travel on the road all day. Definitely want website and phone on vehicles. Check out Hinge Vista.com as well for what they offer us.

Target Market(s)

Commercial Clients looking for fence / gates / gate automation

Industry/Entity Type

Commercial Fence Contruction

Requirements
Must have
• Mention of Commercial Fence / Temp Fence and Gate Automation & Access Controls
Should not have
• Colors that dont match the files I uploaded or colors that are not on my website

```html
<!DOCTYPE html>
<html lang="en">
<head>
<meta charset="utf-8">
<title>Harborline Fence & Post Co — Vehicle Wrap Side Panel</title>
<link href="https://fonts.googleapis.com/css2?family=Cinzel:wght@700&family=Montserrat:wght@500;700&family=Roboto+Condensed:wght@400&display=swap" rel="stylesheet">
<style>
  :root {
    --maroon: #7a1619;
    --maroon-deep: #5a0f12;
    --wrap-black: #0f0f10;
    --swoosh: #e9e9ea;
    --gold: #d9b25c;
    --white: #ffffff;
    --page: #ffffff;
  }
  * { margin: 0; padding: 0; box-sizing: border-box; }
  html, body {
    width: 1200px; height: 675px; overflow: hidden;
    background: var(--page);
  }
  .wrap-panel {
    position: relative;
    width: 1200px; height: 675px;
    overflow: hidden;
  }
  .wrap-graphics { position: absolute; inset: 0; }
  .brand {
    position: absolute;
    left: 230px; top: 252px;
    display: flex; align-items: center; gap: 20px;
  }
  .brand-mark {
    width: 66px; height: 66px;
    background: var(--gold);
    flex: none;
  }
  .brand-name {
    font-family: "Cinzel", serif;
    font-weight: 700;
    color: var(--gold);
    font-size: 33px;
    line-height: 1.1;
    white-space: nowrap;
  }
  .brand-services {
    position: absolute;
    left: 316px; top: 350px;
    font-family: "Cinzel", serif;
    font-weight: 700;
    color: var(--gold);
    font-size: 16px;
    letter-spacing: 0.5px;
    white-space: nowrap;
  }
  .contact {
    position: absolute;
    left: 850px; top: 112px;
    white-space: nowrap;
  }
  .contact-web {
    font-family: "Montserrat", sans-serif;
    font-weight: 500;
    color: var(--white);
    font-size: 16px;
  }
  .contact-phone {
    font-family: "Montserrat", sans-serif;
    font-weight: 700;
    color: var(--gold);
    font-size: 38px;
    margin-top: 6px;
    letter-spacing: -0.5px;
  }
  .service-line {
    position: absolute;
    left: 0; right: 360px; bottom: 22px;
    text-align: center;
    font-family: "Roboto Condensed", sans-serif;
    color: var(--white);
    font-size: 25px;
    white-space: nowrap;
  }
</style>
</head>
<body>
  <main class="wrap-panel">
    <svg class="wrap-graphics" width="1200" height="675" viewBox="0 0 1200 675" aria-hidden="true">
      <defs>
        <linearGradient id="maroonFill" x1="0" y1="0" x2="0" y2="1">
          <stop offset="0" stop-color="#7a1619"/>
          <stop offset="1" stop-color="#5a0f12"/>
        </linearGradient>
      </defs>
      <rect class="body-maroon" width="1200" height="675" fill="url(#maroonFill)"/>
      <path class="swoosh-band" d="M740 0 L830 0 C820 320 760 600 470 600 L420 600 C690 560 750 320 740 0 Z" fill="var(--swoosh)"/>
      <path class="body-black" d="M830 0 L1200 0 L1200 675 L0 675 L0 600 L470 600 C760 600 820 320 830 0 Z" fill="var(--wrap-black)"/>
    </svg>

    <div class="brand">
      <span class="brand-mark"></span>
      <div class="brand-name">Harborline Fence<br>&amp; Post Co</div>
    </div>
    <div class="brand-services">Commercial / Temp Fence</div>

    <div class="contact">
      <div class="contact-web">www.harborlinefenceandpostco.com</div>
      <div class="contact-phone">1-508-555-0147</div>
    </div>

    <p class="service-line">Commercial Fence / Temp Fence and Gate Automation &amp; Access Controls</p>
  </main>
</body>
</html>
```